boosters

revamp current booster flyer - modernize make it look better

please use website
Kestrelmotorhub.co.nz for as much as possible

i want you all to come with own wording description etc

```html
<!DOCTYPE html>
<html lang="en">
<head>
<meta charset="utf-8">
<title>Kestrel Motor Hub – Brake &amp; Clutch Boosters</title>
<link href="https://fonts.googleapis.com/css2?family=Rubik:wght@700;800;900&family=Poppins:ital,wght@0,400;0,500;1,400&display=swap" rel="stylesheet">
<style>
  :root {
    --yellow: #f7d90f;
    --yellow-soft: #f9e04a;
    --black: #111111;
    --panel: #1c1c1c;
    --ink: #1d1d1d;
    --white: #ffffff;
    --page: #a8a8a8;
    --metal-light: #d9d9d9;
  }
  * { margin: 0; padding: 0; box-sizing: border-box; }
  html, body { width: 735px; height: 1200px; overflow: hidden; }
  body { background: var(--page); font-family: "Poppins", sans-serif; color: var(--ink); }

  .flyer {
    position: absolute; left: 0; top: 80px;
    width: 735px; height: 1040px;
    background: var(--white);
    overflow: hidden;
    box-shadow: 0 4px 14px rgba(0,0,0,.25);
  }
  .header-band {
    position: absolute; left: 0; top: 0; width: 735px; height: 317px;
    background: linear-gradient(135deg, var(--yellow) 0%, var(--yellow-soft) 55%, var(--yellow) 100%);
  }

  .brand { position: absolute; left: 50px; top: 46px; width: 240px; font-family: "Rubik", sans-serif; color: var(--black); line-height: .9; white-space: nowrap; }
  .brand__name { display: block; font-weight: 900; font-size: 46px; letter-spacing: -1px; }
  .brand__sub { display: block; font-weight: 800; font-size: 33px; margin-top: 8px; letter-spacing: -.5px; }

  .tagline {
    position: absolute; left: 304px; top: 42px; width: 181px; height: 101px;
    background: var(--white);
    clip-path: polygon(0 0, 100% 0, 100% 82%, 90% 100%, 0 100%);
    padding: 10px 0 0 23px;
    font-size: 22px; line-height: 24px; color: var(--black);
  }

  .brand-mark {
    position: absolute; left: 508px; top: 40px; width: 166px;
    display: flex; flex-direction: column; align-items: center; gap: 12px;
    font-family: "Rubik", sans-serif; font-weight: 700; font-size: 13.5px; color: var(--black);
    letter-spacing: .3px; white-space: nowrap;
  }
  .brand-mark__square { width: 72px; height: 72px; background: var(--black); }

  .title-panel {
    position: absolute; left: 44px; top: 184px; width: 647px; height: 199px;
    background: linear-gradient(160deg, #2a2a2a 0%, var(--panel) 50%, #0d0d0d 100%);
    border-top: 3px solid var(--white);
    clip-path: polygon(0 0, 100% 0, 100% 72%, 91% 100%, 0 100%);
    text-align: center; font-family: "Rubik", sans-serif;
  }
  .title-panel__line { display: block; font-weight: 800; font-size: 61px; line-height: 60px; letter-spacing: -.5px; }
  .title-panel__line--white { color: var(--white); margin-top: 20px; }
  .title-panel__line--yellow { color: var(--yellow); }
  .title-panel__sub { display: block; font-family: "Poppins", sans-serif; font-size: 24px; color: var(--white); margin-top: 6px; }

  .product { position: absolute; border-radius: 40%; }
  .product--dark { background: radial-gradient(ellipse at 40% 35%, #5a5a5a 0%, #1b1b1b 60%, #0a0a0a 100%); }
  .product--metal { background: radial-gradient(ellipse at 40% 35%, #e9e4da 0%, #b9b2a4 60%, #8d887e 100%); }

  .features {
    position: absolute; left: 44px; top: 742px; width: 327px; height: 166px;
    background: var(--yellow);
    clip-path: polygon(0 0, 100% 0, 100% 70%, 86% 100%, 0 100%);
  }
  .feature {
    position: absolute; display: flex; gap: 8px;
    font-size: 19px; line-height: 22px; color: var(--ink);
  }
  .feature svg { flex: none; margin-top: 3px; }
  .features__note { position: absolute; left: 32px; top: 130px; font-size: 15px; color: var(--ink); }

  .about { position: absolute; left: 402px; top: 746px; width: 300px; font-size: 17.5px; line-height: 22px; font-weight: 500; color: var(--black); }
  .about__rule { width: 52px; height: 2px; background: var(--yellow); margin: 12px 0 12px; }

  .footer {
    position: absolute; left: 0; top: 929px; width: 735px; height: 111px;
    background: linear-gradient(180deg, #3a3a3a 0%, #141414 30%, #050505 100%);
    border-top: 3px solid var(--metal-light);
    color: var(--white); font-size: 15px;
  }
  .contact { position: absolute; display: flex; align-items: center; gap: 8px; white-space: nowrap; }
  .contact svg { flex: none; }
  .footer__name {
    position: absolute; left: 330px; top: 44px; width: 80px; text-align: center;
    font-family: "Rubik", sans-serif; font-weight: 700; font-size: 16px; color: var(--white);
  }
  .footer__unsubscribe { position: absolute; left: 452px; top: 76px; font-size: 12.5px; font-style: italic; color: var(--yellow); }
</style>
</head>
<body>
<main class="flyer">
  <div class="header-band"></div>

  <h1 class="brand"><span class="brand__name">KESTREL</span><span class="brand__sub">Motor Hub</span></h1>

  <p class="tagline">The Brake<br>and Cable<br>Specialists</p>

  <div class="brand-mark"><span class="brand-mark__square"></span><span>KESTREL MOTOR HUB</span></div>

  <section class="title-panel">
    <span class="title-panel__line title-panel__line--white">BRAKE &amp; CLUTCH</span>
    <span class="title-panel__line title-panel__line--yellow">BOOSTERS</span>
    <span class="title-panel__sub">Suppliers and repairers</span>
  </section>

  <div class="product product--dark" role="img" aria-label="Photo of a truck air brake booster" style="left:76px;top:418px;width:258px;height:122px;"></div>
  <div class="product product--dark" role="img" aria-label="Photo of a vacuum brake booster with reservoir" style="left:500px;top:428px;width:162px;height:130px;"></div>
  <div class="product product--metal" role="img" aria-label="Photo of two alloy brake master cylinders" style="left:84px;top:575px;width:180px;height:138px;"></div>
  <div class="product product--dark" role="img" aria-label="Photo of a clutch booster unit" style="left:274px;top:522px;width:214px;height:166px;"></div>
  <div class="product product--dark" role="img" aria-label="Photo of a remote vacuum booster" style="left:512px;top:604px;width:142px;height:114px;"></div>

  <section class="features">
    <div class="feature" style="left:32px;top:20px;"><svg width="18" height="18" viewBox="0 0 18 18"><circle cx="9" cy="9" r="9" fill="#fff"/><path d="M5 9.3l2.6 2.6L13 6.4" fill="none" stroke="#111" stroke-width="2"/></svg><span>Truck<br>Boosters</span></div>
    <div class="feature" style="left:177px;top:20px;"><svg width="18" height="18" viewBox="0 0 18 18"><circle cx="9" cy="9" r="9" fill="#fff"/><path d="M5 9.3l2.6 2.6L13 6.4" fill="none" stroke="#111" stroke-width="2"/></svg><span>Clutch<br>Boosters</span></div>
    <div class="feature" style="left:32px;top:75px;"><svg width="18" height="18" viewBox="0 0 18 18"><circle cx="9" cy="9" r="9" fill="#fff"/><path d="M5 9.3l2.6 2.6L13 6.4" fill="none" stroke="#111" stroke-width="2"/></svg><span>Vacuum<br>Boosters</span></div>
    <div class="feature" style="left:177px;top:75px;"><svg width="18" height="18" viewBox="0 0 18 18"><circle cx="9" cy="9" r="9" fill="#fff"/><path d="M5 9.3l2.6 2.6L13 6.4" fill="none" stroke="#111" stroke-width="2"/></svg><span>Remotes<br>Boosters</span></div>
    <p class="features__note">Also supply parts and kits etc.</p>
  </section>

  <section class="about">
    <p>Kestrel Motor Hub specialise in the Re-Manufacture of Brakes, Hoses and Cables</p>
    <div class="about__rule"></div>
    <p>Our aim is to repair parts with the quickest turn-around times possible</p>
  </section>

  <footer class="footer">
    <div class="contact" style="left:56px;top:16px;"><svg width="16" height="16" viewBox="0 0 16 16"><circle cx="8" cy="8" r="8" fill="#f7d90f"/><path d="M8 3.5a3 3 0 0 0-3 3c0 2.2 3 5.8 3 5.8s3-3.6 3-5.8a3 3 0 0 0-3-3z" fill="#111"/><circle cx="8" cy="6.5" r="1.1" fill="#f7d90f"/></svg><span>42 Tarrant Road, Hamilton</span></div>
    <div class="contact" style="left:56px;top:42px;"><svg width="16" height="16" viewBox="0 0 16 16"><circle cx="8" cy="8" r="8" fill="#f7d90f"/><rect x="4" y="5" width="8" height="6" fill="none" stroke="#111" stroke-width="1.2"/><path d="M4 5l4 3.3L12 5" fill="none" stroke="#111" stroke-width="1.2"/></svg><span>parts@kestrelmotorhub.co.nz</span></div>
    <div class="contact" style="left:56px;top:68px;"><svg width="16" height="16" viewBox="0 0 16 16"><circle cx="8" cy="8" r="8" fill="#f7d90f"/><circle cx="8" cy="8" r="4.2" fill="none" stroke="#111" stroke-width="1.1"/><path d="M3.8 8h8.4M8 3.8c-2 2.4-2 6 0 8.4M8 3.8c2 2.4 2 6 0 8.4" fill="none" stroke="#111" stroke-width="1"/></svg><span>www.kestrelmotorhub.co.nz</span></div>

    <div class="footer__name">KESTREL</div>

    <div class="contact" style="left:428px;top:20px;"><svg width="16" height="16" viewBox="0 0 16 16"><circle cx="8" cy="8" r="8" fill="#f7d90f"/><path d="M5.2 4.2l1.6-.4 1 2.2-1 .8a6 6 0 0 0 2.4 2.4l.8-1 2.2 1-.4 1.6c-3.3.3-6.9-3.3-6.6-6.6z" fill="#111"/></svg><span>Free Phone - 0800 55 61 20</span></div>
    <div class="contact" style="left:452px;top:46px;"><span>Ph 07 555 0142 | Fax 07 555 0143</span></div>
    <div class="footer__unsubscribe">Unsubscribe from this list</div>
  </footer>
</main>
</body>
</html>
```